Property development & Investment company Need a logo & business card design

Our name is KT Estates Australia Pty Ltd
Need logo & business card design

Target Market(s)

People dealing in commercial property

Industry/Entity Type

Business

Contact Information for Business Card

KT Estates Australia
Peter Dunmore Mobile0419 703 646
Email Peter@quillbarrow.com.au

Font styles to use
Sans Serif

Requirements
Must have
• company name
• contact details
Nice to have
• KT Estates Bold
• Australia Not Bold
Should not have
• To busy of a look

```html
<!DOCTYPE html>
<html lang="en">
<head>
<meta charset="utf-8">
<title>KT Estates Australia – Business Card</title>
<link href="https://fonts.googleapis.com/css2?family=Ubuntu:wght@400;500;700&display=swap" rel="stylesheet">
<style>
  :root {
    --backdrop: #8a949e;
    --card: #ffffff;
    --card-shade: #f1f1f1;
    --brand-dark: #3a0f0c;
    --name-green: #0f5a2c;
    --rule: #8c6a62;
    --contact: #3a3a3a;
    --skyline-light: #ececec;
    --skyline-mid: #e0e0e0;
  }
  html, body {
    margin: 0;
    padding: 0;
    width: 1200px;
    height: 675px;
    overflow: hidden;
    background: var(--backdrop);
    font-family: "Ubuntu", sans-serif;
  }
  .stage {
    width: 1200px;
    height: 675px;
    display: flex;
    align-items: center;
    justify-content: center;
  }
  .business-card {
    position: relative;
    width: 980px;
    height: 560px;
    background: linear-gradient(160deg, var(--card) 0%, var(--card) 55%, var(--card-shade) 100%);
    overflow: hidden;
  }
  .skyline-art {
    position: absolute;
    left: 120px;
    right: 0;
    bottom: 0;
    height: 330px;
    background: linear-gradient(180deg, var(--skyline-light) 0%, var(--skyline-mid) 100%);
    clip-path: polygon(0 100%, 0 72%, 18% 48%, 36% 42%, 44% 28%, 56% 20%, 66% 0, 78% 12%, 88% 4%, 100% 14%, 100% 100%);
    opacity: 0.75;
  }
  .brand {
    position: absolute;
    top: 120px;
    left: 0;
    right: 0;
    display: flex;
    align-items: center;
    justify-content: center;
    gap: 14px;
  }
  .brand-mark {
    width: 22px;
    height: 22px;
    background: var(--brand-dark);
  }
  .brand-name {
    font-weight: 700;
    font-size: 46px;
    color: var(--brand-dark);
    letter-spacing: 0.5px;
  }
  .contact-block {
    position: absolute;
    right: 70px;
    top: 330px;
    width: 560px;
  }
  .person-name {
    margin: 0;
    text-align: right;
    font-weight: 700;
    font-size: 38px;
    color: var(--name-green);
    padding-right: 130px;
  }
  .divider {
    border: 0;
    border-top: 1.5px solid var(--rule);
    margin: 10px 0 12px;
  }
  .contact-line {
    margin: 0;
    font-size: 22px;
    color: var(--contact);
    letter-spacing: 0.3px;
  }
</style>
</head>
<body>
<main class="stage">
  <section class="business-card">
    <div class="skyline-art" role="img" aria-label="Faint grey harbour skyline with arch bridge and sail-roofed building"></div>
    <header class="brand">
      <span class="brand-mark"></span>
      <span class="brand-name">KT Estates Australia</span>
    </header>
    <div class="contact-block">
      <h1 class="person-name">Peter Dunmore</h1>
      <hr class="divider">
      <p class="contact-line">M. 0438 512 907 | E. peter@quillbarrow.com.au</p>
    </div>
  </section>
</main>
</body>
</html>
```